Eye Doctor Needs Updated Business Card

We need a standard US business card designed for an optometrist's practice. Our practice name is Halvorn Vision Center and attached you'll find our logos. We are located in a smaller community, we are a trusted source for eye care and designer eyewear. We have 2 different version of our logos, so both versions are attached. Our slogan is "Close to Home, Clear in Focus". I'd like to see designs with one of our logos on the front with our contact info, and have the slogan on the back by itself. Final design should be professional looking, include the colors of our logo or colors that compliment the logo. We want it to look appropriate for a healthcare practice but also up-to-date, eye-catching, to have the normal contact info like address, phone #, email, but also possibly room for additional contact info such as facebook.
Updates

I just uploaded .eps files to use instead of the jpeg. Hope that helps!

So many great designs! We tending to like the darker blues that are used in our logo as the main blue color for the business cards. We also really like the use of a water-mark type appearance on either the front and/or back, or the embossed look as well looks nice. Thank you all for such great designs!

We're preferring the designs where white and the darker blue used in our logo are the primary colors on the front, but with a little green used as well. Again though, thanks for all the impressive designs so far!

Industry/Entity Type

Healthcare

```html
<!DOCTYPE html>
<html lang="en">
<head>
<meta charset="utf-8">
<title>Halvorn Vision Center – Business Card</title>
<link href="https://fonts.googleapis.com/css2?family=Open+Sans:ital,wght@0,400;0,600;1,400&display=swap" rel="stylesheet">
<style>
  :root {
    --navy: #173c66;
    --navy-deep: #12335a;
    --blue: #2a86c8;
    --blue-bright: #3aa0dc;
    --green: #3a9a35;
    --green-text: #1f5e1c;
    --white: #f4f5f5;
    --muted: #dde7f0;
    --stage: #e4e4e4;
  }
  * { box-sizing: border-box; margin: 0; padding: 0; }
  html, body { width: 1200px; height: 1200px; overflow: hidden; }
  body {
    background: radial-gradient(circle at 50% 30%, #f5f5f5 0%, var(--stage) 75%);
    font-family: "Open Sans", Arial, sans-serif;
    position: relative;
  }
  .card {
    position: absolute;
    left: 320px;
    width: 560px;
    height: 320px;
    overflow: hidden;
    background: var(--white);
    box-shadow: 0 6px 18px rgba(0,0,0,0.18);
  }
  .card--back { top: 230px; }
  .card--front { top: 650px; }

  /* Back side */
  .back-blue {
    position: absolute; left: 0; top: 0; width: 310px; height: 100%;
    background: radial-gradient(circle at 100% 40%, var(--blue-bright) 0%, var(--blue) 30%, var(--navy-deep) 85%);
  }
  .back-green {
    position: absolute; left: 310px; top: 0; right: 0; height: 100%;
    background: var(--green);
  }
  .back-band {
    position: absolute; left: 95px; right: 0; top: 118px; height: 100px;
    background: var(--white);
    display: flex; align-items: center; padding-left: 30px;
  }
  .slogan {
    position: absolute; left: 170px; top: 84px;
    color: var(--muted); font-size: 14px; font-style: italic; letter-spacing: 0.2px;
    white-space: nowrap;
  }

  .brand { display: flex; align-items: center; gap: 12px; white-space: nowrap; }
  .brand__dot {
    width: 44px; height: 44px; border-radius: 50%;
    background: var(--navy);
    flex: none;
  }
  .brand__name {
    color: var(--navy); font-weight: 600; font-size: 25px; letter-spacing: 0.5px;
  }

  /* Front side */
  .front-blue { position: absolute; inset: 0; }
  .name-band {
    position: absolute; left: 0; top: 42px; width: 330px; height: 50px;
    background: var(--green);
    padding: 8px 0 0 60px;
    color: var(--green-text); font-size: 13px; line-height: 17px;
  }
  .address {
    position: absolute; left: 48px; top: 114px; width: 190px;
    color: var(--muted); font-size: 13px; line-height: 17px;
  }
  .front-brand { position: absolute; left: 266px; top: 118px; }
  .front-brand .brand__name { font-size: 19px; letter-spacing: 0.3px; }
  .front-brand .brand__dot { width: 34px; height: 34px; }
  .accent-square {
    position: absolute; right: 0; top: 162px; width: 30px; height: 40px;
    background: var(--green);
  }
  .contacts {
    position: absolute; left: 262px; top: 220px;
    list-style: none; color: var(--white); font-size: 14px; line-height: 22px;
    white-space: nowrap;
  }
  .contacts li { display: flex; align-items: center; gap: 6px; }
  .contacts svg { width: 14px; height: 14px; flex: none; }
</style>
</head>
<body>

  <section class="card card--back" aria-label="Card back">
    <div class="back-blue" role="img" aria-label="Deep blue field with soft radial glow"></div>
    <div class="back-green"></div>
    <p class="slogan">"Close to Home, Clear in Focus"</p>
    <div class="back-band">
      <div class="brand">
        <span class="brand__dot"></span>
        <span class="brand__name">Halvorn Vision Center</span>
      </div>
    </div>
  </section>

  <section class="card card--front" aria-label="Card front">
    <svg class="front-blue" width="560" height="320" viewBox="0 0 560 320" aria-hidden="true">
      <defs>
        <linearGradient id="frontBlue" x1="0" y1="0" x2="1" y2="0.4">
          <stop offset="0" stop-color="#12335a"/>
          <stop offset="0.55" stop-color="#1d4f82"/>
          <stop offset="1" stop-color="#2f8fd0"/>
        </linearGradient>
      </defs>
      <polygon points="0,96 250,96 250,210 560,210 560,320 0,320" fill="url(#frontBlue)"/>
    </svg>
    <div class="name-band">Name : xxxxxxx xx<br>xxxxxxx xxxxx</div>
    <p class="address">address : xxxxxxx xx xxxxx, xxxxxxx xxxxx xxxxxxxx, xxxxx</p>
    <div class="brand front-brand">
      <span class="brand__dot"></span>
      <span class="brand__name">Halvorn Vision Center</span>
    </div>
    <div class="accent-square"></div>
    <ul class="contacts">
      <li>
        <svg viewBox="0 0 14 14"><rect x="0" y="0" width="14" height="14" rx="2" fill="#dde7f0"/><path d="M4 3h2l1 3-1.5 1a6 6 0 0 0 2.5 2.5L9 8l3 1v2a1 1 0 0 1-1 1A9 9 0 0 1 3 4a1 1 0 0 1 1-1z" fill="#173c66"/></svg>
        (000) 000-0000
      </li>
      <li>
        <svg viewBox="0 0 14 14"><rect x="0" y="0" width="14" height="14" rx="2" fill="#dde7f0"/></svg>
        (000) 000-0000 for room
      </li>
      <li>
        <svg viewBox="0 0 14 14"><rect x="0" y="0" width="14" height="14" rx="2" fill="#dde7f0"/><path d="M2.5 4.5h9v5.5h-9z M2.5 4.5l4.5 3.5 4.5-3.5" fill="none" stroke="#173c66" stroke-width="1.1"/></svg>
        xxxxxxxxxxxxxxxxxxxxxxxxx.com
      </li>
    </ul>
  </section>

</body>
</html>
```